Bluebird Listings ad 2014 15

I need a design for an advertisement in our Bluebird Listings book telephone directory.
The directory runs for a 12 month period.

Our business offers 24 hour glass replacements to homes, shops and offices.
Our service is usually required by customers that require their glass replaced urgently
.
The ad is 1 of many in the directory offering the same service so we need to attract the customers attention quickly and easily and deliver our message - "24hr glass replacements to doors windows and shopfronts. Call now 9372 4816".

I want to keep the data in the attached ad but with a professional graphic presentation.

The ad size is 58mm high x 83mm wide, full colour.

Target Market(s)

Our customer is generally someone in need of an emergency repair. They aren't spending time shopping around for a product, they have a problem that they want fixed promptly and professionally.

Industry/Entity Type

Business

Font styles to use
Sans Serif

Colors
0255a3
f37022

Requirements
Must have
• "24HR" must stand out, this is a key aspect of our service. The ad needs to be clear and easy to read.

```html
<!DOCTYPE html>
<html lang="en">
<head>
<meta charset="utf-8">
<title>Steadfast Glass – 24HR Glass Replacements</title>
<link rel="stylesheet" href="https://fonts.googleapis.com/css2?family=Open+Sans:wght@400;500;600;700;800&display=swap">
<style>
  :root {
    --brand-blue: #0255a3;
    --brand-orange: #f37022;
    --sky-deep: #4fb6ea;
    --sky-mid: #9fd8f5;
    --sky-light: #eaf7fd;
    --ink: #111111;
    --navy: #0d2a4a;
    --logo-blue: #2b6f9c;
    --white: #ffffff;
  }
  html, body {
    margin: 0;
    padding: 0;
    width: 1200px;
    height: 838px;
    overflow: hidden;
    background: var(--white);
  }
  .ad {
    position: relative;
    width: 1200px;
    height: 838px;
    overflow: hidden;
    font-family: "Open Sans", sans-serif;
    background:
      radial-gradient(ellipse 620px 380px at 600px 470px, var(--sky-light) 0%, rgba(234,247,253,0) 100%),
      linear-gradient(180deg, var(--sky-mid) 0%, var(--sky-deep) 55%, var(--sky-mid) 100%);
  }
  .ad p, .ad h1 { white-space: nowrap; }
  .crack {
    position: absolute;
    border-radius: 50%;
    background: radial-gradient(circle, rgba(255,255,255,0.55) 0%, rgba(255,255,255,0) 70%);
  }
  .crack--left { left: -60px; top: 380px; width: 300px; height: 320px; }
  .crack--right { right: -40px; top: 560px; width: 300px; height: 300px; }

  .headline-band {
    position: absolute;
    left: 0;
    top: 0;
    width: 1200px;
    height: 260px;
  }
  .hook {
    position: absolute;
    right: 24px;
    top: 4px;
    margin: 0;
    font-size: 76px;
    font-weight: 800;
    color: var(--brand-orange);
    letter-spacing: 1px;
    line-height: 1;
  }
  .hours {
    position: absolute;
    left: 22px;
    top: 66px;
    margin: 0;
    font-size: 180px;
    font-weight: 800;
    color: var(--ink);
    line-height: 1;
    letter-spacing: -6px;
  }
  .service {
    position: absolute;
    left: 520px;
    top: 104px;
    margin: 0;
    font-size: 73px;
    font-weight: 600;
    color: var(--ink);
    line-height: 1;
    letter-spacing: -1px;
  }
  .service-scope {
    position: absolute;
    left: 524px;
    top: 188px;
    margin: 0;
    font-size: 37px;
    font-weight: 600;
    color: var(--ink);
    line-height: 1;
  }
  .promise {
    position: absolute;
    left: 0;
    width: 1200px;
    top: 268px;
    margin: 0;
    text-align: center;
    font-size: 33px;
    font-weight: 400;
    color: var(--navy);
    line-height: 1.2;
  }
  .credentials {
    position: absolute;
    left: 0;
    width: 1200px;
    top: 316px;
    margin: 0;
    text-align: center;
    font-size: 28px;
    font-weight: 400;
    color: var(--navy);
    line-height: 1.2;
  }
  .call-to-action {
    position: absolute;
    left: 0;
    width: 1200px;
    top: 374px;
    margin: 0;
    text-align: center;
    font-size: 182px;
    font-weight: 500;
    color: var(--ink);
    line-height: 1;
    letter-spacing: -2px;
  }
  .phone {
    position: absolute;
    left: 0;
    width: 1200px;
    top: 506px;
    margin: 0;
    text-align: center;
    font-size: 196px;
    font-weight: 700;
    color: var(--ink);
    line-height: 1;
    letter-spacing: -2px;
  }
  .brand-name {
    position: absolute;
    left: 0;
    width: 1200px;
    top: 722px;
    margin: 0;
    text-align: center;
    font-size: 48px;
    font-weight: 600;
    color: var(--logo-blue);
    line-height: 1;
  }
  .brand-tagline {
    position: absolute;
    left: 0;
    width: 1200px;
    top: 780px;
    margin: 0;
    text-align: center;
    font-size: 28px;
    font-weight: 400;
    color: var(--navy);
    line-height: 1;
  }
</style>
</head>
<body>
<main class="ad">
  <div class="crack crack--left" role="img" aria-label="Shattered glass crack lines"></div>
  <div class="crack crack--right" role="img" aria-label="Shattered glass crack lines"></div>

  <svg class="headline-band" viewBox="0 0 1200 260" aria-hidden="true">
    <path d="M500 0 H1200 V91 H500 Z" fill="var(--white)" opacity="0.35"/>
    <path d="M50 91 H1200 V240 H50 Q12 240 12 202 V129 Q12 91 50 91 Z" fill="var(--brand-orange)"/>
  </svg>

  <p class="hook">BROKEN GLASS?</p>
  <h1 class="hours">24HR</h1>
  <p class="service">glass replacements</p>
  <p class="service-scope">to doors windows and shopfronts</p>

  <p class="promise">To regain the Safety and Security in your home, shop or office.</p>
  <p class="credentials">- Qualified trandsmen - All work guaranteed - Insurance billed direct -</p>

  <p class="call-to-action">CALL NOW</p>
  <p class="phone">9372 4816</p>

  <p class="brand-name">steadfastglass</p>
  <p class="brand-tagline">the trusted name in glass replacement</p>
</main>
</body>
</html>
```